PIETRO business card - High end Italian floors and coverings

We need a new design for our business card. We are an exclusive company located in Mexico.
Our commercial name is PIETRO. Our legal name is Grande Volta SA de CV.
We bring the latest trends in materials for floors and walls such as natural stones, wood, leather, design porcelanato tiles and so.
Our company image colors are black, white and red.
Our customers are high end architects and designers.
We are looking for an elegant but fresh design which reflects exclusivity, simplicity and reliability.
(we are working also in a new website)

Requirements
Nice to have
• back and front design
Space for 2 addresses (one for each showroom location)

```html
<!DOCTYPE html>
<html lang="es">
<head>
<meta charset="utf-8">
<title>PIETRO – Tarjeta de presentación</title>
<link rel="stylesheet" href="https://fonts.googleapis.com/css2?family=Quicksand:wght@300;400&family=Cormorant+Garamond:wght@500&display=swap">
<style>
  :root {
    --card-black: #0c0c0c;
    --brand-red: #c8000a;
    --band-red: #c60000;
    --ink-white: #f2f2f2;
    --backdrop: #ece9e4;
  }
  * { margin: 0; padding: 0; box-sizing: border-box; }
  html, body { width: 1200px; height: 1000px; overflow: hidden; }
  body {
    position: relative;
    background: var(--backdrop);
    font-family: "Quicksand", sans-serif;
    color: var(--ink-white);
  }
  .card {
    position: absolute;
    top: 245px;
    width: 540px;
    height: 310px;
    background: var(--card-black);
    box-shadow: 0 6px 18px rgba(0,0,0,.18);
    overflow: hidden;
  }
  .card--front { left: 45px; }
  .card--back { left: 615px; }

  .accent-line {
    position: absolute;
    left: 58px;
    width: 2px;
    background: var(--brand-red);
  }
  .accent-line--top { top: 0; height: 100px; }
  .accent-line--bottom { bottom: 0; height: 18px; }

  .holder { position: absolute; left: 58px; top: 116px; }
  .holder__name {
    font-weight: 300;
    font-size: 34px;
    letter-spacing: 1.5px;
    line-height: 1;
    white-space: nowrap;
    color: var(--ink-white);
  }
  .holder__surname { color: var(--brand-red); }
  .holder__email {
    margin-top: 8px;
    font-weight: 400;
    font-size: 13px;
    letter-spacing: .8px;
  }

  .showroom {
    position: absolute;
    font-size: 12px;
    letter-spacing: .6px;
    line-height: 18px;
    list-style: none;
    white-space: nowrap;
  }
  .showroom--guadalajara { left: 58px; top: 196px; }
  .showroom--cdmx { left: 280px; top: 214px; }
  .showroom li { display: flex; gap: 6px; }
  .showroom li.indent { padding-left: 19px; }
  .showroom svg { width: 13px; height: 13px; margin-top: 2px; flex: none; }

  .back-brand {
    position: absolute;
    inset: 0;
    display: flex;
    flex-direction: column;
    align-items: center;
    justify-content: center;
    gap: 10px;
  }
  .back-brand__name {
    font-family: "Cormorant Garamond", serif;
    font-weight: 500;
    font-size: 54px;
    letter-spacing: 6px;
    color: var(--ink-white);
  }
  .back-brand__legal {
    font-family: "Cormorant Garamond", serif;
    font-weight: 500;
    font-size: 12px;
    letter-spacing: 3px;
    color: var(--ink-white);
  }

  .brand-band {
    position: absolute;
    left: 0; top: 815px;
    width: 1200px; height: 185px;
    background: var(--band-red);
    display: flex;
    align-items: center;
    justify-content: center;
  }
  .brand-band__name {
    font-family: "Cormorant Garamond", serif;
    font-weight: 500;
    font-size: 74px;
    letter-spacing: 5px;
    color: #fff;
  }
</style>
</head>
<body>

<svg width="0" height="0" style="position:absolute">
  <defs>
    <symbol id="icon-home" viewBox="0 0 14 14">
      <rect x="0" y="0" width="14" height="14" rx="2" fill="#f2f2f2"/>
      <path d="M3 7 L7 3.5 L11 7 M4.5 6 V10.5 H9.5 V6" fill="none" stroke="#0c0c0c" stroke-width="1.4"/>
    </symbol>
    <symbol id="icon-phone" viewBox="0 0 14 14">
      <rect x="0" y="0" width="14" height="14" rx="2" fill="#f2f2f2"/>
      <path d="M3 5.5 Q7 2.5 11 5.5 L10 7 H4 Z" fill="#0c0c0c"/>
      <rect x="4" y="7.5" width="6" height="3.5" fill="#0c0c0c"/>
    </symbol>
    <symbol id="icon-mobile" viewBox="0 0 14 14">
      <rect x="0" y="0" width="14" height="14" rx="2" fill="#f2f2f2"/>
      <rect x="4.5" y="2.5" width="5" height="9" rx="1" fill="none" stroke="#0c0c0c" stroke-width="1.3"/>
    </symbol>
  </defs>
</svg>

<section class="card card--front" aria-label="Frente de tarjeta">
  <span class="accent-line accent-line--top"></span>
  <span class="accent-line accent-line--bottom"></span>

  <div class="holder">
    <p class="holder__name">Carla <span class="holder__surname">Reyes Bastian</span></p>
    <p class="holder__email">carla@pietro.com.mx</p>
  </div>

  <ul class="showroom showroom--guadalajara">
    <li><svg><use href="#icon-home"/></svg>Cristal 1820 Col. Arcos</li>
    <li class="indent">Guadalajara, Jal</li>
    <li><svg><use href="#icon-phone"/></svg>(33) 3402 7715</li>
    <li><svg><use href="#icon-mobile"/></svg>(33) 1750 4283</li>
  </ul>

  <ul class="showroom showroom--cdmx">
    <li><svg><use href="#icon-home"/></svg>Lago Alberto 340 B</li>
    <li class="indent">Col. Granada, Del. Miguel Hidalgo</li>
    <li class="indent">Mexico D.F.</li>
    <li><svg><use href="#icon-phone"/></svg>(55) 5281 4609</li>
  </ul>
</section>

<section class="card card--back" aria-label="Reverso de tarjeta">
  <div class="back-brand">
    <p class="back-brand__name">PIETRO</p>
    <p class="back-brand__legal">GRANDE VOLTA SA DE CV</p>
  </div>
</section>

<footer class="brand-band">
  <p class="brand-band__name">PIETRO</p>
</footer>

</body>
</html>
```